" Oferecemos serviço de elaboração de planejamento e orçamento de obras, acompanhamento de reformas, vistorias e elaboração de laudos e pareces, projetos para empreendimentos residenciais e comerciais (fundações, arquitetônico, estrutural, elétrico, hidrossanitário, telecomunicação, gesso, piso, gás, entre outros), consultoria para implantar sistemas de gestão de produtos e processos, análise da viabilidade econômico-financeira, levando em conta estimativa de custos e mercado de trabalho e por fim, administração de obras, incluindo acompanhamento de obras, contratação da mão de obra e controle de orçamento. "

```html
<!DOCTYPE html>
<html lang="pt-BR">
<head>
<meta charset="utf-8">
<title>Veltra Engenharia — Cartão de visita</title>
<link rel="stylesheet" href="https://fonts.googleapis.com/css2?family=Montserrat:wght@400;600;700;800&display=swap">
<style>
  :root {
    --navy: #183a55;
    --ink: #1e2430;
    --teal: #4fa8b4;
    --paper: #ffffff;
    --paper-shade: #e9ecef;
    --stage: #e4e4e2;
    --text-muted: #5b6470;
  }
  * { box-sizing: border-box; margin: 0; padding: 0; }
  html, body { width: 1200px; height: 1200px; overflow: hidden; }
  body {
    background: var(--stage);
    font-family: "Montserrat", Arial, sans-serif;
    position: relative;
  }
  .card {
    position: absolute;
    left: 215px;
    width: 770px;
    height: 440px;
    overflow: hidden;
    box-shadow: 0 6px 18px rgba(0,0,0,.18);
  }
  /* Front */
  .card--front {
    top: 130px;
    background: linear-gradient(160deg, var(--paper) 45%, var(--paper-shade) 100%);
  }
  .front-mark {
    position: absolute;
    left: 70px;
    top: 150px;
    display: flex;
    align-items: center;
    gap: 16px;
    color: var(--navy);
    font-weight: 800;
    font-size: 54px;
    letter-spacing: 2px;
  }
  .front-mark .square {
    width: 26px; height: 26px; background: var(--navy);
  }
  .identity {
    position: absolute;
    left: 402px;
    top: 78px;
    text-align: center;
  }
  .identity .name {
    font-weight: 700;
    font-size: 28px;
    color: var(--navy);
  }
  .identity .role {
    font-size: 13px;
    letter-spacing: 3px;
    color: var(--text-muted);
    margin-top: 2px;
  }
  .contacts {
    position: absolute;
    left: 402px;
    top: 196px;
    list-style: none;
  }
  .contacts li {
    display: flex;
    align-items: center;
    gap: 18px;
    font-size: 14px;
    font-weight: 600;
    color: var(--navy);
    line-height: 1.35;
    margin-bottom: 22px;
  }
  .contacts .icon {
    flex: none;
    width: 26px; height: 26px;
    background: var(--navy);
    border-radius: 3px;
    display: flex; align-items: center; justify-content: center;
  }
  .contacts .icon svg { width: 16px; height: 16px; }
  .contacts .address { font-size: 12.5px; }
  .front-band {
    position: absolute;
    left: 0; bottom: 14px;
    width: 100%; height: 14px;
  }
  /* Back */
  .card--back {
    top: 620px;
    background: var(--ink);
  }
  .back-mark {
    position: absolute;
    left: 0; right: 0;
    top: 150px;
    text-align: center;
    color: var(--paper);
    font-weight: 700;
  }
  .back-mark .square {
    width: 22px; height: 22px; background: var(--paper);
    margin: 0 auto 26px;
  }
  .back-mark .word {
    font-size: 62px;
    letter-spacing: 4px;
    line-height: 1;
  }
  .back-mark .sub {
    font-size: 22px;
    letter-spacing: 12px;
    margin-top: 10px;
    padding-left: 12px;
  }
  .back-band {
    position: absolute;
    left: 0; bottom: 12px;
    width: 100%; height: 12px;
    background: var(--teal);
  }
</style>
</head>
<body>

<section class="card card--front">
  <div class="front-mark"><span class="square"></span>VELTRA</div>

  <div class="identity">
    <p class="name">Nome Sobrenome</p>
    <p class="role">Diretor Comercial</p>
  </div>

  <ul class="contacts">
    <li>
      <span class="icon"><svg viewBox="0 0 16 16" fill="none" stroke="#fff" stroke-width="1.6"><rect x="2" y="4" width="12" height="8"/><path d="M2 4l6 5 6-5"/></svg></span>
      contato@veltraeng.com.br
    </li>
    <li>
      <span class="icon"><svg viewBox="0 0 16 16" fill="#fff"><path d="M4 2h3l1 3-2 1a8 8 0 0 0 4 4l1-2 3 1v3a1 1 0 0 1-1 1A11 11 0 0 1 3 3a1 1 0 0 1 1-1z"/></svg></span>
      <span>(11) 0000-0000<br>(11) 00000-0000</span>
    </li>
    <li>
      <span class="icon"><svg viewBox="0 0 16 16" fill="none" stroke="#fff" stroke-width="1.4"><circle cx="8" cy="8" r="6"/><ellipse cx="8" cy="8" rx="2.6" ry="6"/><path d="M2 8h12"/></svg></span>
      www.veltraengenharia.com.br
    </li>
    <li>
      <span class="icon"><svg viewBox="0 0 16 16" fill="#fff"><path d="M8 1a5 5 0 0 0-5 5c0 4 5 9 5 9s5-5 5-9a5 5 0 0 0-5-5zm0 7a2 2 0 1 1 0-4 2 2 0 0 1 0 4z"/></svg></span>
      <span class="address">Rua do projeto, 00 Centro - Cidade - Estado<br>Cep. 00.000.000</span>
    </li>
  </ul>

  <svg class="front-band" viewBox="0 0 770 14" preserveAspectRatio="none">
    <polygon points="0,4 640,4 636,14 0,14" fill="#183a55"/>
    <polygon points="660,0 770,0 770,14 652,14" fill="#4fa8b4"/>
  </svg>
</section>

<section class="card card--back">
  <div class="back-mark">
    <div class="square"></div>
    <p class="word">VELTRA</p>
    <p class="sub">ENGENHARIA</p>
  </div>
  <div class="back-band"></div>
</section>

</body>
</html>
```